I need a Funnel Image/graphic for each bonus product offered in my Harbor Ledger Course..

The Harbor Ledger Mentor BONUS: Scholarship ($5000)
BONUS: Pro Bono FCRA and FCDPA violation legal representation by a Credit Law Firm ($4997)
BONUS: Harbor Ledger Expert Book
BONUS: 4 Months FREE Credit Repair Coaching Your Price Today ($1495)
BONUS: FREE Dispute Letters Your Price Today ($997)
BONUS: Private Chatterloop Group Access ($497)
BONUS: Credit Rebuilding Strategies Course Your Price Today ($497)
BONUS: Credit File Audit Your Price Today ($297)
BONUS: Credit Education Book
BONUS: 1-on-1 Strategy Consultation Call With a Member of Tobias's Team ($297)
Everyday Price: ($9997)
Your Savings Today: ($14077)
Your Price Today: $4997.00 (one time payment)

```html
<!DOCTYPE html>
<html lang="en">
<head>
<meta charset="utf-8">
<title>The Harbor Ledger Expert – Cover</title>
<link rel="stylesheet" href="https://fonts.googleapis.com/css2?family=Oswald:wght@500;600;700&family=Open+Sans:wght@600;700;800&display=swap">
<style>
  :root{
    --page:#ececec;
    --cover:#fbfaf6;
    --ink:#2b2b2b;
    --gold-light:#e8c766;
    --gold:#c9a13a;
    --gold-dark:#9a7520;
    --red:#c0222b;
    --maroon:#8e1a1f;
    --green:#7cb82f;
    --orange:#e8782a;
    --sky:#3ab0e0;
    --blue:#2a5fb0;
    --white:#ffffff;
  }
  html,body{margin:0;padding:0;overflow:hidden;}
  body{width:1200px;height:1200px;background:var(--page);display:flex;align-items:center;justify-content:center;}
  .cover{
    position:relative;width:700px;height:1120px;background:var(--cover);
    box-shadow:0 6px 24px rgba(0,0,0,.18);
    display:flex;flex-direction:column;align-items:center;box-sizing:border-box;padding-top:70px;
  }
  .title{margin:0;text-align:center;font-family:'Oswald',sans-serif;line-height:.95;}
  .title-the{display:block;font-size:68px;font-weight:600;color:var(--ink);letter-spacing:2px;}
  .title-key{display:block;font-size:170px;font-weight:700;letter-spacing:2px;
    background:linear-gradient(180deg,var(--gold-light) 0%,var(--gold) 55%,var(--gold-dark) 100%);
    -webkit-background-clip:text;background-clip:text;color:transparent;}
  .title-rest{display:block;font-size:76px;font-weight:500;color:var(--ink);letter-spacing:3px;margin-top:6px;}
  .subtitle{margin:22px 0 0;font-family:'Open Sans',sans-serif;font-weight:700;font-size:25px;line-height:1.25;color:var(--ink);text-align:center;}
  .funnel{margin-top:26px;width:660px;height:430px;}
  .funnel text{font-family:'Open Sans',sans-serif;}
  .author{position:absolute;bottom:50px;margin:0;font-family:'Oswald',sans-serif;font-weight:600;font-size:52px;letter-spacing:5px;color:var(--ink);}
</style>
</head>
<body>
<main class="cover">
  <h1 class="title">
    <span class="title-the">THE</span>
    <span class="title-key">HARBOR</span>
    <span class="title-rest">LEDGER EXPERT</span>
  </h1>
  <p class="subtitle">Discover the Fourth Score Secretly<br>Used by Banks and Financial Institutions</p>

  <svg class="funnel" viewBox="0 0 660 430" xmlns="http://www.w3.org/2000/svg">
    <defs>
      <linearGradient id="presenterTone" x1="0" y1="0" x2="0" y2="1">
        <stop offset="0" stop-color="#e6b48a"/>
        <stop offset=".45" stop-color="#b5473a"/>
        <stop offset="1" stop-color="#5a3a30"/>
      </linearGradient>
    </defs>

    <!-- presenter figure area -->
    <rect class="presenter" x="530" y="60" width="105" height="260" rx="10" fill="url(#presenterTone)" role="img" aria-label="Cartoon presenter in a brown jacket pointing toward the price tag"/>

    <!-- header row -->
    <g class="funnel-header">
      <polygon points="80,28 290,28 290,48 80,48" fill="var(--red)"/>
      <text x="185" y="43" font-size="13" font-weight="700" fill="var(--white)" text-anchor="middle">Harbor Ledger Expert Book</text>
      <polygon points="340,28 540,28 520,48 340,48" fill="var(--maroon)"/>
      <text x="430" y="43" font-size="13" font-weight="700" fill="var(--white)" text-anchor="middle">Credit Education Book</text>
      <circle cx="315" cy="30" r="26" fill="var(--red)" stroke="var(--gold)" stroke-width="3"/>
      <text x="315" y="35" font-size="13" font-weight="800" fill="var(--gold-light)" text-anchor="middle">Bonus</text>
    </g>

    <!-- bonus bands -->
    <g class="funnel-bands" font-size="12" font-weight="700" fill="var(--white)">
      <polygon points="20,56 510,56 495,84 20,84" fill="var(--red)"/>
      <text x="34" y="75" font-size="13">1. The Harbor Ledger Mentor Scholarship</text>
      <text x="480" y="75" text-anchor="end">$5000</text>

      <polygon points="28,88 500,88 485,116 28,116" fill="var(--green)"/>
      <text x="42" y="100" font-size="10.5">2. Pro Bono FCRA and FCDPA violation</text>
      <text x="42" y="112" font-size="10.5">legal representation by a Credit Law Firm</text>
      <text x="470" y="107" text-anchor="end">$4997</text>

      <polygon points="36,120 490,120 475,148 36,148" fill="var(--orange)"/>
      <text x="50" y="139" textLength="355" lengthAdjust="spacingAndGlyphs">3. 4 Months FREE Credit Repair Coaching Your Price Today</text>
      <text x="460" y="139" text-anchor="end">$1495</text>

      <polygon points="44,152 480,152 465,180 44,180" fill="var(--red)"/>
      <text x="58" y="171">4. FREE Dispute Letters Your Price Today</text>
      <text x="450" y="171" text-anchor="end">$997</text>

      <polygon points="52,184 470,184 455,212 52,212" fill="var(--orange)"/>
      <text x="66" y="203">5. Private Chatterloop Group Access</text>
      <text x="440" y="203" text-anchor="end">$497</text>

      <polygon points="60,216 460,216 445,244 60,244" fill="var(--green)"/>
      <text x="74" y="235" textLength="312" lengthAdjust="spacingAndGlyphs">6. Credit Rebuilding Strategies Course Your Price Today</text>
      <text x="430" y="235" text-anchor="end">$497</text>

      <polygon points="68,248 450,248 435,276 68,276" fill="var(--sky)"/>
      <text x="82" y="267">7. Credit File Audit Your Price Today</text>
      <text x="420" y="267" text-anchor="end">$297</text>

      <polygon points="76,280 440,280 425,308 76,308" fill="var(--blue)"/>
      <text x="90" y="298" font-size="10" textLength="280" lengthAdjust="spacingAndGlyphs">8. 1-on-1 Strategy Consultation Call With a Member of Tobias's Team</text>
      <text x="410" y="298" text-anchor="end">$297</text>
    </g>

    <!-- totals band -->
    <g class="funnel-totals">
      <rect x="20" y="320" width="620" height="40" fill="var(--maroon)"/>
      <text x="40" y="346" font-size="18" font-weight="700" fill="var(--white)">Everyday Price  $9997</text>
      <text x="625" y="346" font-size="18" font-weight="700" fill="var(--white)" text-anchor="end">Your Savings Today  $14077</text>
    </g>

    <!-- price tag -->
    <g class="price-tag">
      <rect x="470" y="232" width="110" height="56" rx="6" fill="var(--red)" stroke="var(--white)" stroke-width="2"/>
      <text x="525" y="249" font-size="11" font-weight="700" fill="var(--white)" text-anchor="middle">Your Price Today</text>
      <text x="525" y="267" font-size="15" font-weight="800" fill="var(--white)" text-anchor="middle">$4997.00</text>
      <text x="525" y="281" font-size="9" font-weight="600" fill="var(--white)" text-anchor="middle">(one time payment)</text>
    </g>
  </svg>

  <p class="author">TOBIAS E. BROWN</p>
</main>
</body>
</html>
```